Wine Label front and back- Need to have an eye catching, classy wine label for restaurant placement.

label design for a wine label. eye catching for shelf placement. looking for simple and elegant label. Name of the vineyard will be the label recognition. Need back label to match with coloring and basic regulated info required by gov't (producer, address, and statement) Back label will be addressed after selected front label to match.
Will add $100 extra for the back label to match.

Target Market(s)

40-65 year old foodies

Colors
0355a3
eaf1f7

Requirements
Must have
• FERNHOLLOW (label name)
Estate,
Red Wine Blend NV,

```html
<!DOCTYPE html>
<html lang="en">
<head>
<meta charset="utf-8">
<title>Fernhollow Estate – Front Label</title>
<link rel="stylesheet" href="https://fonts.googleapis.com/css2?family=Playfair+Display:wght@500;600&family=Noto+Serif:wght@400&display=swap">
<style>
  :root {
    --navy: #0f3f85;
    --brand-blue: #0355a3;
    --mist: #eaf1f7;
    --mist-deep: #d6e2ec;
    --silver-dark: #9aa6ae;
    --silver-light: #f4f6f7;
    --white: #ffffff;
  }
  * { margin: 0; padding: 0; box-sizing: border-box; }
  html, body {
    width: 1200px;
    height: 1059px;
    overflow: hidden;
    background: var(--white);
  }
  .canvas {
    position: relative;
    width: 1200px;
    height: 1059px;
  }
  .label {
    position: absolute;
    left: 260px;
    top: 82px;
    width: 680px;
    height: 895px;
    overflow: hidden;
  }
  .label__field {
    position: absolute;
    inset: 0 0 217px 0;
    background: linear-gradient(180deg, var(--mist) 0%, #f2f6fa 50%, var(--mist) 100%);
  }
  .label__top-tab {
    position: absolute;
    left: 82px;
    top: 0;
    width: 275px;
    height: 29px;
    background: var(--navy);
  }
  .label__title {
    position: absolute;
    left: 84px;
    top: 455px;
    font-family: "Playfair Display", serif;
    font-weight: 600;
    font-size: 78px;
    line-height: 1;
    letter-spacing: 1px;
    color: var(--navy);
  }
  .label__subtitle {
    position: absolute;
    left: 0;
    top: 543px;
    width: 380px;
    height: 39px;
    background: var(--navy);
    color: var(--white);
    font-family: "Noto Serif", serif;
    font-size: 29px;
    line-height: 39px;
    padding-left: 86px;
    white-space: nowrap;
  }
  .label__silver-rule {
    position: absolute;
    left: 0;
    top: 650px;
    width: 680px;
    height: 28px;
    background: linear-gradient(90deg, var(--silver-dark) 0%, var(--silver-light) 35%, #c3ccd2 60%, var(--silver-light) 80%, var(--silver-dark) 100%);
  }
  .label__base {
    position: absolute;
    left: 0;
    top: 678px;
    width: 680px;
    height: 217px;
    background: linear-gradient(180deg, var(--navy) 0%, #12458f 50%, var(--navy) 100%);
  }
  .label__name {
    position: absolute;
    left: 0;
    top: 0;
    width: 680px;
    height: 217px;
  }
  .label__name text {
    font-family: "Playfair Display", serif;
    font-weight: 500;
    font-size: 104px;
  }
</style>
</head>
<body>
  <main class="canvas">
    <section class="label" aria-label="Fernhollow Estate front wine label">
      <div class="label__field" role="img" aria-label="Pale blue field of fine wavy lines"></div>
      <div class="label__top-tab"></div>
      <h1 class="label__title">ESTATE</h1>
      <p class="label__subtitle">Red Wine Blend NV</p>
      <div class="label__silver-rule"></div>
      <div class="label__base" role="img" aria-label="Navy band with subtle wavy lines">
        <svg class="label__name" viewBox="0 0 680 217" aria-label="FERNHOLLOW">
          <defs>
            <linearGradient id="silver" x1="0" y1="0" x2="0" y2="1">
              <stop offset="0" stop-color="#f4f6f7"/>
              <stop offset="0.5" stop-color="#c3ccd2"/>
              <stop offset="1" stop-color="#e6eaec"/>
            </linearGradient>
          </defs>
          <text x="340" y="142" text-anchor="middle" fill="url(#silver)" textLength="600" lengthAdjust="spacingAndGlyphs">FERNHOLLOW</text>
        </svg>
      </div>
    </section>
  </main>
</body>
</html>
```